Need a logo/cover design for my book Golden Handshake Hours: How We Turned Coffee Chats Into Fortunes With Friends Worth Keeping

Over the years I've worked in chambers of commerce and at high-profile country clubs and have had access to very successful people and the companies they work for or launch. Through meeting people, learning from them, applying what I've learned, and by connecting with them as resources and lead sources for business, I've been able to generate over $2M in the past few years. I'm sharing the roadmap I followed to create the connections and make the sales.
Updates

Combination of slow feedback on my part by not understanding the process, similar designs, and many who withdrew immediately after my first response.

Target Market(s)

Entrepreneurs and business people, specifically business owners and those in sales and marketing roles.

Industry/Entity Type

Small Business

Font styles to use
Sans Serif

Colors

Designer to choose colors to be used in the design.

Requirements
Must have
• Original graphic design. Something that looks like I paid a professional to have it done.
Nice to have
• Perhaps my picture? Not really sure
Should not have
• I'd like to avoid a look that I could have created myself using clip art and special fonts.

```html
<!DOCTYPE html>
<html lang="en">
<head>
<meta charset="utf-8">
<title>Golden Handshake Hours — Book Cover</title>
<link href="https://fonts.googleapis.com/css2?family=Cabin:wght@500;600;700&family=Montserrat:wght@600;700&display=swap" rel="stylesheet">
<style>
  :root {
    --orange: #f26a2e;
    --charcoal: #3e3e40;
    --charcoal-soft: #55565a;
    --white: #ffffff;
    --backdrop: #efe3d6;
  }
  html, body {
    margin: 0;
    width: 1200px;
    height: 754px;
    overflow: hidden;
    background: var(--backdrop);
  }
  .book-cover {
    position: absolute;
    left: 309px;
    top: 0;
    width: 582px;
    height: 754px;
    display: block;
  }
  .brand-name {
    font-family: "Montserrat", sans-serif;
    font-weight: 700;
    font-size: 27px;
    fill: var(--orange);
    letter-spacing: 1px;
  }
  .title { font-family: "Cabin", sans-serif; }
  .title-white { fill: var(--white); font-weight: 500; }
  .title-accent {
    fill: var(--orange);
    font-weight: 700;
    stroke: var(--white);
    stroke-width: 3px;
    paint-order: stroke;
  }
  .band-label {
    font-family: "Montserrat", sans-serif;
    font-weight: 700;
    font-size: 23px;
    fill: var(--white);
    letter-spacing: 0.5px;
  }
</style>
</head>
<body>
<svg class="book-cover" viewBox="0 0 582 754" xmlns="http://www.w3.org/2000/svg">
  <defs>
    <linearGradient id="buildingTone" x1="0" y1="0" x2="0" y2="1">
      <stop offset="0" stop-color="#4a4a4d"/>
      <stop offset="0.6" stop-color="#3e3e40"/>
      <stop offset="1" stop-color="#444447"/>
    </linearGradient>
  </defs>

  <!-- Cover base -->
  <rect class="cover-base" x="0" y="0" width="582" height="754" fill="var(--white)"/>

  <!-- Brand header -->
  <g class="brand-header">
    <circle cx="96" cy="78" r="14" fill="var(--orange)"/>
    <text class="brand-name" x="122" y="88">GOLDEN HANDSHAKE HOURS</text>
  </g>

  <!-- Title panel with building photo area -->
  <rect class="photo-panel" x="0" y="140" width="582" height="458" fill="url(#buildingTone)"
        role="img" aria-label="Muted grey photograph of a classical building facade"/>

  <!-- Orange diagonal wedge with white divider -->
  <polygon class="wedge-divider" points="561,140 582,140 582,598 381,598" fill="var(--white)"/>
  <polygon class="wedge" points="570,140 582,140 582,598 392,598" fill="var(--orange)"/>

  <!-- Title -->
  <g class="title">
    <text class="title-white" x="20" y="244"><tspan font-size="40">HOW </tspan><tspan font-size="54">WE TURNED</tspan></text>
    <text class="title-accent" x="18" y="314" font-size="88">COFFEE</text>
    <text class="title-accent" x="18" y="384" font-size="88">CHATS</text>
    <text class="title-white" x="20" y="436"><tspan font-size="44">INTO </tspan><tspan font-size="58">FORTUNES</tspan></text>
    <text class="title-white" x="20" y="484"><tspan font-size="44">WITH </tspan><tspan font-size="58">FRIENDS</tspan></text>
    <text class="title-white" x="20" y="526" font-size="44">WORTH KEEPING</text>
  </g>

  <!-- Bottom band -->
  <g class="footer-band">
    <rect x="0" y="620" width="582" height="110" fill="var(--orange)"/>
    <polygon points="468,620 508,620 452,730 412,730" fill="var(--white)"/>
    <polygon points="474,620 504,620 448,730 418,730" fill="var(--charcoal)"/>
    <polygon points="512,620 530,620 474,730 456,730" fill="var(--white)"/>
    <polygon points="518,620 548,620 492,730 462,730" fill="var(--charcoal)"/>
    <text class="band-label" x="24" y="683">GOLDEN HANDSHAKE HOURS</text>
  </g>
</svg>
</body>
</html>
```